Brindle Search Business Card for recruitment company

We are looking for a Business Card Design that incorporates our personal details and our busines name and logo. We are a specialized search consultancy that recruit Property and Construction professionals.
We would like a business card that stands out and is appealing to the Construction and Property industry as well.

Target Market(s)

people in the construction and property industry

Contact Information for Business Card

Business Name and logo

Font styles to use
Serif

Colors
0094D4
00A9DD
6FCCEA
C7EBF8
E9F6FB

Requirements
Must have
• Business name and logo as well as contact details
Should not have
• No photos of us please

```html
<!DOCTYPE html>
<html lang="en">
<head>
<meta charset="utf-8">
<title>Brindle Search – Business Card</title>
<link rel="stylesheet" href="https://fonts.googleapis.com/css2?family=Josefin+Sans:wght@300;400&family=Montserrat:wght@400;500;700&display=swap">
<style>
  :root {
    --teal-deep: #0d3f57;
    --teal-band: #0f4460;
    --blue-bright: #1a8fc9;
    --white: #ffffff;
    --stage: #e9eef1;
  }
  html, body {
    margin: 0;
    padding: 0;
    width: 1200px;
    height: 912px;
    overflow: hidden;
    background: var(--stage);
  }
  .canvas {
    position: relative;
    width: 1200px;
    height: 912px;
  }
  .card {
    position: absolute;
    width: 600px;
    height: 343px;
    border-radius: 4px;
    overflow: hidden;
    box-shadow: 0 6px 18px rgba(0, 0, 0, 0.18);
  }
  /* Front */
  .card--front {
    left: 90px;
    top: 80px;
    background: var(--teal-deep);
  }
  .front-pattern {
    position: absolute;
    inset: 0;
    background: linear-gradient(120deg, var(--teal-deep) 30%, #125a7e 65%, var(--blue-bright) 100%);
  }
  .front-wordmark {
    position: absolute;
    left: 0;
    right: 0;
    top: 148px;
    text-align: center;
    font-family: "Josefin Sans", sans-serif;
    font-weight: 300;
    font-size: 46px;
    letter-spacing: 3px;
    color: var(--white);
  }
  /* Back */
  .card--back {
    left: 510px;
    top: 490px;
    background: var(--white);
  }
  .back-band {
    position: absolute;
    left: 0;
    right: 0;
    bottom: 0;
    height: 128px;
    background: var(--teal-band);
  }
  .back-block {
    position: absolute;
    right: 0;
    top: 70px;
    width: 170px;
    bottom: 0;
    background: var(--teal-band);
  }
  .back-mark {
    position: absolute;
    right: 42px;
    top: 100px;
  }
  .back-wordmark {
    position: absolute;
    left: 44px;
    top: 62px;
    font-family: "Josefin Sans", sans-serif;
    font-weight: 300;
    font-size: 34px;
    letter-spacing: 2px;
    color: var(--teal-band);
  }
  .person {
    position: absolute;
    left: 44px;
    top: 150px;
    font-family: "Montserrat", sans-serif;
    color: var(--teal-band);
  }
  .person-name {
    margin: 0;
    font-size: 19px;
    font-weight: 700;
    letter-spacing: 1px;
  }
  .person-role {
    margin: 2px 0 0;
    font-size: 13px;
    color: #222;
  }
  .contact {
    position: absolute;
    left: 44px;
    bottom: 14px;
    margin: 0;
    padding: 0;
    list-style: none;
    font-family: "Montserrat", sans-serif;
    font-size: 13px;
    line-height: 19px;
    color: var(--white);
  }
  .contact-gap { margin-top: 4px; }
  .contact li { display: flex; align-items: center; gap: 7px; }
  .contact svg { width: 11px; height: 11px; flex: none; }
</style>
</head>
<body>
<main class="canvas">
  <section class="card card--front">
    <div class="front-pattern" role="img" aria-label="Repeating brand-mark pattern in deep teal fading to bright blue"></div>
    <div class="front-wordmark">BRINDLE SEARCH</div>
  </section>

  <section class="card card--back">
    <div class="back-band"></div>
    <div class="back-block"></div>
    <svg class="back-mark" width="86" height="86" viewBox="0 0 86 86" aria-hidden="true">
      <circle cx="43" cy="43" r="38" fill="none" stroke="var(--white)" stroke-width="6"/>
    </svg>
    <div class="back-wordmark">BRINDLE SEARCH</div>
    <div class="person">
      <p class="person-name">MARCUS HALE</p>
      <p class="person-role">Director</p>
    </div>
    <ul class="contact">
      <li>418 Cedar Row</li>
      <li>Salem, OR 97301</li>
      <li class="contact-gap">
        <svg viewBox="0 0 12 12"><path d="M2.5 1 L4.5 1 L5.5 3.5 L4.2 4.6 Q5.2 6.8 7.4 7.8 L8.5 6.5 L11 7.5 L11 9.5 Q10.5 11 9 11 Q1 10 1 2.5 Q1 1 2.5 1 Z" fill="var(--white)"/></svg>
        (555) 014-2290
      </li>
      <li>
        <svg viewBox="0 0 12 12"><rect x="1" y="2.5" width="10" height="7" fill="none" stroke="var(--white)" stroke-width="1.2"/><path d="M1 2.5 L6 6.5 L11 2.5" fill="none" stroke="var(--white)" stroke-width="1.2"/></svg>
        hello@brindlesearch.com
      </li>
      <li>
        <svg viewBox="0 0 12 12"><circle cx="6" cy="6" r="5" fill="none" stroke="var(--white)" stroke-width="1.1"/><ellipse cx="6" cy="6" rx="2.2" ry="5" fill="none" stroke="var(--white)" stroke-width="1"/><line x1="1" y1="6" x2="11" y2="6" stroke="var(--white)" stroke-width="1"/></svg>
        www.brindlesearch.com
      </li>
    </ul>
  </section>
</main>
</body>
</html>
```